Website re-design for a Gardening - Vegetable Growing -Compost Ecommerce site

We need a "green & organic" looking web design for The Loamfield Store website re-design. The website sells garden and landscape supplies, and specialises in composites and vegetable growing products which are sold nationwide throughout the UK.

This project is for a homepage & content page design which can be used as a template to create other pages through the site, ideally with css and coding for a joomla template.

Our customer base is made up of gardeners & vegetable growers. The site is an ecommerce site run on Joomla CMS, we will be converting the design into a joomla template.

The Home page will contain information and attractive garden & vegetable growing images linking to information and product / shop category pages.

Current site: www.theloamfieldstore.co.uk

Sites I like the look of :

http://fernpatchplanter.com/index.php
http://keepsake.brovelmedia.com
http://www.tumblerootfolk.co.uk/
http://www.hamletcreamery.co.uk
Updates

Hi Guys! Feel free to use different colour schemes from the three colours i have suggested in the brief. I am open to any suggestions, but a modern look and feel is preferred.

Target Market(s)

Home owners, vegetable growers and keen gardeners

Industry/Entity Type

Landscape

Coding

Coded - Design and coding required

Font styles to use
Sans Serif

Colors
9bcb3c
faa54b
fece3e

Requirements
Must have
• a white main content background

```html
<!DOCTYPE html>
<html lang="en">
<head>
<meta charset="utf-8">
<title>The Loamfield Store – Home</title>
<link href="https://fonts.googleapis.com/css2?family=Questrial&family=Open+Sans:wght@400;700&family=Roboto:wght@400&display=swap" rel="stylesheet">
<style>
  :root {
    --green: #9bcb3c;
    --green-dark: #4aa63c;
    --green-deep: #3d9a35;
    --mint: #6ccfa2;
    --red-tick: #d8433a;
    --ink: #333;
    --muted: #666;
    --line: #dedede;
    --white: #fff;
    --sky: #dbeefa;
  }
  * { box-sizing: border-box; margin: 0; padding: 0; }
  html, body { width: 948px; height: 1200px; overflow: hidden; background: var(--white); }
  body { position: relative; font-family: "Roboto", Arial, sans-serif; color: var(--ink); }
  .abs { position: absolute; }

  /* header */
  .site-header { position: absolute; left: 0; top: 0; width: 948px; height: 161px;
    background: linear-gradient(180deg, var(--sky) 0%, var(--white) 45%); }
  .brand { display: flex; align-items: center; gap: 9px; white-space: nowrap; }
  .brand-mark { width: 32px; height: 32px; border-radius: 50%; background: #f6c324; flex: none; }
  .brand-name { font-family: "Questrial", sans-serif; color: var(--green-dark); font-size: 25px; line-height: 1; }
  .header-brand { left: 133px; top: 38px; }
  .account-links { left: 598px; top: 27px; font-size: 9.5px; color: var(--muted); display: flex; gap: 5px; align-items: center; font-family: "Open Sans", sans-serif; white-space: nowrap; }
  .account-links .cart { display: flex; align-items: center; gap: 6px; margin-right: 12px; }
  .phone { left: 700px; top: 51px; font-size: 15px; color: var(--ink); display: flex; align-items: center; gap: 7px; white-space: nowrap; }
  .main-nav { left: 124px; top: 112px; display: flex; font-family: "Questrial", sans-serif; font-size: 11.5px; color: #555; white-space: nowrap; }
  .main-nav a { text-decoration: none; color: inherit; padding: 6px 15px; border-left: 1px solid var(--line); }
  .main-nav a:first-child { border-left: 0; padding-left: 10px; }

  /* hero */
  .hero { left: 0; top: 161px; width: 948px; height: 338px;
    background: radial-gradient(ellipse at 20% 90%, #c1602e 0%, #6f7a2e 25%, transparent 45%),
                linear-gradient(90deg, #8ab0cf 0%, #6f8a55 30%, #6d8d3a 60%, #a7b968 100%); }
  .hero-caption { left: 259px; top: 274px; width: 689px; height: 94px; background: rgba(140,190,50,.82); padding: 12px 28px; }
  .hero-caption h1 { font-family: "Questrial", sans-serif; font-weight: 400; font-size: 21px; color: #1a2a0c; letter-spacing: -.2px; white-space: nowrap; }
  .hero-caption p { font-size: 13px; color: #223; line-height: 1.25; margin-top: 4px; }
  .hero-dots { left: 770px; top: 465px; display: flex; gap: 4px; }
  .hero-dots span { width: 8px; height: 8px; border-radius: 50%; background: rgba(255,255,255,.6); }
  .hero-dots span:first-child { background: var(--white); }

  /* featured */
  .section-title { font-family: "Questrial", sans-serif; font-size: 22px; color: #555; font-weight: 400; white-space: nowrap; }
  .section-title em { font-style: normal; color: var(--green); }
  .featured-title { left: 133px; top: 534px; }
  .view-all { left: 488px; top: 533px; width: 124px; height: 27px; border: 1px solid #ccc; font-family: "Questrial", sans-serif; font-size: 10px; color: #888; display: flex; align-items: center; justify-content: center; gap: 6px; white-space: nowrap; }
  .carousel { left: 133px; top: 576px; width: 497px; height: 201px; }
  .carousel-arrow { position: absolute; top: 0; width: 16px; height: 201px; background: var(--green); }
  .carousel-arrow.left { left: 0; } .carousel-arrow.right { right: 0; }
  .carousel-arrow svg { position: absolute; top: 86px; left: 3px; }
  .product { position: absolute; top: 0; width: 152px; height: 201px; border: 1px solid var(--line); box-shadow: 0 0 0 1px #f1f1f1 inset; }
  .product h3 { font-family: "Questrial", sans-serif; font-weight: 400; font-size: 12px; color: #333; padding: 10px 0 0 14px; width: 124px; line-height: 1.15; height: 40px; }
  .product-img { margin: 4px auto 0; width: 72px; height: 98px; border-radius: 3px; }
  .buy-btn { position: absolute; left: 35px; bottom: 5px; width: 80px; height: 19px; border-radius: 10px; background: var(--green); color: var(--white); font-family: "Open Sans", sans-serif; font-weight: 700; font-size: 9.5px; display: flex; align-items: center; justify-content: center; gap: 4px; white-space: nowrap; }

  /* promo */
  .promo-cloud { left: 641px; top: 524px; width: 172px; height: 142px; }
  .promo-text { left: 664px; top: 549px; width: 126px; text-align: center; color: var(--white); font-family: "Open Sans", sans-serif; font-weight: 700; font-size: 12px; line-height: 1.3; }
  .perks { left: 664px; top: 672px; list-style: none; font-family: "Questrial", sans-serif; font-size: 13px; color: #444; }
  .perks li { display: flex; align-items: center; gap: 5px; height: 18px; white-space: nowrap; }
  .order-btn { left: 679px; top: 756px; width: 92px; height: 20px; border-radius: 10px; background: var(--green); color: var(--white); font-family: "Open Sans", sans-serif; font-weight: 700; font-size: 10px; display: flex; align-items: center; justify-content: center; white-space: nowrap; }

  /* welcome */
  .welcome-title { left: 147px; top: 848px; }
  .welcome-copy { left: 147px; top: 896px; width: 436px; font-family: Arial, "Roboto", sans-serif; font-size: 10px; line-height: 14.4px; color: #444; }
  .welcome-copy p + p { margin-top: 12px; }
  .welcome-photo { left: 611px; top: 848px; width: 209px; height: 136px; background: linear-gradient(180deg, #9aa8a4 0%, #70786a 40%, #3a2c22 70%, #2b211a 100%); }
  .readmore { left: 145px; top: 997px; width: 88px; height: 25px; border-radius: 13px; background: var(--green-dark); color: var(--white); font-family: "Open Sans", sans-serif; font-weight: 700; font-size: 10px; display: flex; align-items: center; justify-content: center; }

  /* footer */
  .footer-rule { left: 0; width: 948px; height: 1px; background: var(--line); }
  .footer-brand { left: 148px; top: 1094px; gap: 8px; }
  .footer-brand .brand-name { font-size: 17px; }
  .footer-brand .brand-mark { width: 26px; height: 26px; }
  .newsletter { left: 356px; top: 1089px; width: 214px; height: 31px; border: 1px solid var(--green-dark); font-family: "Questrial", sans-serif; font-size: 9.5px; color: #777; display: flex; align-items: center; justify-content: space-between; padding: 0 10px 0 12px; white-space: nowrap; }
  .send-btn { left: 574px; top: 1089px; width: 85px; height: 31px; background: var(--green-dark); color: var(--white); font-family: "Open Sans", sans-serif; font-weight: 700; font-size: 10px; display: flex; align-items: center; justify-content: center; }
  .social { left: 722px; top: 1100px; display: flex; gap: 8px; }
  .social span { width: 9px; height: 9px; border-radius: 50%; background: var(--green-dark); }
  .copyright { left: 0; top: 1156px; width: 948px; text-align: center; font-size: 11px; color: var(--green-deep); }
</style>
</head>
<body>

<header class="site-header">
  <div class="abs brand header-brand"><span class="brand-mark"></span><span class="brand-name">The Loamfield Store</span></div>
  <div class="abs account-links">
    <span class="cart">
      <svg width="13" height="11" viewBox="0 0 13 11"><path d="M0 1h2.5l1.6 6h7l1.4-4.5H3.3" fill="none" stroke="#4aa63c" stroke-width="1.6"/><circle cx="5" cy="9.5" r="1.1" fill="#4aa63c"/><circle cx="10" cy="9.5" r="1.1" fill="#4aa63c"/></svg>
      0 - item
    </span>
    <span>My Account</span>|<span>My Wishlist</span>|<span>Checkout</span>
  </div>
  <div class="abs phone">
    <svg width="14" height="14" viewBox="0 0 14 14"><circle cx="7" cy="7" r="7" fill="#4aa63c"/><path d="M4.3 3.8l1.3-.3.8 1.8-.8.7c.4.9 1.1 1.6 2 2l.7-.8 1.8.8-.3 1.3c-3 .2-5.7-2.5-5.5-5.5z" fill="#fff"/></svg>
    (818) 555 01942
  </div>
  <nav class="abs main-nav">
    <a href="#">HOME</a><a href="#">PRODUCTS</a><a href="#">ABOUT US</a><a href="#">WHAT WE DO</a><a href="#">GARDEN GURU</a><a href="#">BLOG</a><a href="#">BULK LOADS</a><a href="#">CONTACT US</a>
  </nav>
</header>

<section class="abs hero" role="img" aria-label="Photo of a gardener holding a crate of freshly harvested carrots, beetroot and lettuce"></section>
<div class="abs hero-caption">
  <h1>Huge Range From Multi Purpose To Specialist Compost Products !</h1>
  <p>We Supply a huge Range of compost products including organic composts, peat free compost, ericaceous composts etc all at unbeatable prices!</p>
</div>
<div class="abs hero-dots"><span></span><span></span><span></span></div>

<h2 class="abs section-title featured-title"><em>FEATURED</em> PRODUCTS</h2>
<div class="abs view-all">
  <svg width="11" height="11" viewBox="0 0 11 11"><circle cx="4.5" cy="4.5" r="3.5" fill="none" stroke="#888" stroke-width="1.2"/><path d="M7 7l3.3 3.3" stroke="#888" stroke-width="1.3"/><path d="M2.8 4.5h3.4M4.5 2.8v3.4" stroke="#888"/></svg>
  VIEW ALL PRODUCTS
</div>

<div class="abs carousel">
  <div class="carousel-arrow left"><svg width="10" height="30" viewBox="0 0 10 30"><path d="M8 1L2 15l6 14" fill="none" stroke="#fff" stroke-width="1.2"/></svg></div>
  <article class="product" style="left:18px">
    <h3 style="width:110px">Organic Compost Bulk Bag</h3>
    <div class="product-img" role="img" aria-label="Purple multipurpose compost bag with flowers" style="background:linear-gradient(180deg,#3b6b3a 0%,#5a2f6e 40%,#4a1d5c 100%)"></div>
    <div class="buy-btn">BUY NOW <svg width="13" height="10" viewBox="0 0 13 10"><path d="M0 1h2.3l1.5 5.5h6.7l1.4-4H3" fill="none" stroke="#fff" stroke-width="1.4"/><circle cx="5" cy="8.6" r="1" fill="#fff"/><circle cx="9.7" cy="8.6" r="1" fill="#fff"/></svg></div>
  </article>
  <article class="product" style="left:172px">
    <h3 style="width:100px">Children’s Veg Garden</h3>
    <div class="product-img" role="img" aria-label="Small seedling sprouting from a mound of soil" style="background:radial-gradient(ellipse at 50% 85%,#5a4030 0%,#8a6a50 35%,#fff 65%)"></div>
    <div class="buy-btn">BUY NOW <svg width="13" height="10" viewBox="0 0 13 10"><path d="M0 1h2.3l1.5 5.5h6.7l1.4-4H3" fill="none" stroke="#fff" stroke-width="1.4"/><circle cx="5" cy="8.6" r="1" fill="#fff"/><circle cx="9.7" cy="8.6" r="1" fill="#fff"/></svg></div>
  </article>
  <article class="product" style="left:327px">
    <h3>Mushroom Compost</h3>
    <div class="product-img" role="img" aria-label="Green bag of mushroom compost" style="background:linear-gradient(180deg,#2f7a3a 0%,#2a6233 100%)"></div>
    <div class="buy-btn">BUY NOW <svg width="13" height="10" viewBox="0 0 13 10"><path d="M0 1h2.3l1.5 5.5h6.7l1.4-4H3" fill="none" stroke="#fff" stroke-width="1.4"/><circle cx="5" cy="8.6" r="1" fill="#fff"/><circle cx="9.7" cy="8.6" r="1" fill="#fff"/></svg></div>
  </article>
  <div class="carousel-arrow right"><svg width="10" height="30" viewBox="0 0 10 30"><path d="M2 1l6 14-6 14" fill="none" stroke="#fff" stroke-width="1.2"/></svg></div>
</div>

<svg class="abs promo-cloud" viewBox="0 0 172 142" aria-hidden="true">
  <path d="M30 112c-18 0-28-14-24-30-10-12-4-32 12-34 0-20 22-34 40-24 10-18 40-20 52-4 16-8 38 2 40 22 18 4 24 26 12 40 6 18-8 34-26 30-6 8-18 10-28 6l-8 22-12-22c-10 4-24 2-30-6-8 4-22 4-28 0z" fill="#6ccfa2"/>
  <text x="12" y="46" fill="#fff" font-size="26" font-family="Georgia, serif">“</text>
  <text x="146" y="114" fill="#fff" font-size="26" font-family="Georgia, serif">”</text>
</svg>
<div class="abs promo-text">Order online before 1.00pm for next day delivery or book a delivery date!</div>
<ul class="abs perks">
  <li><svg width="14" height="13" viewBox="0 0 14 13"><rect x=".5" y="2.5" width="10" height="10" fill="#fff" stroke="#888"/><path d="M2.5 7l3 3 7-9" fill="none" stroke="#d8433a" stroke-width="2"/></svg>Great Value</li>
  <li><svg width="14" height="13" viewBox="0 0 14 13"><rect x=".5" y="2.5" width="10" height="10" fill="#fff" stroke="#888"/><path d="M2.5 7l3 3 7-9" fill="none" stroke="#d8433a" stroke-width="2"/></svg>Quality Service</li>
  <li><svg width="14" height="13" viewBox="0 0 14 13"><rect x=".5" y="2.5" width="10" height="10" fill="#fff" stroke="#888"/><path d="M2.5 7l3 3 7-9" fill="none" stroke="#d8433a" stroke-width="2"/></svg>Fast Delivery</li>
  <li><svg width="14" height="13" viewBox="0 0 14 13"><rect x=".5" y="2.5" width="10" height="10" fill="#fff" stroke="#888"/><path d="M2.5 7l3 3 7-9" fill="none" stroke="#d8433a" stroke-width="2"/></svg>The Finest Products</li>
</ul>
<div class="abs order-btn">ORDER ONLINE</div>

<h2 class="abs section-title welcome-title">WELCOME TO THE <em>LOAMFIELD STORE</em></h2>
<div class="abs welcome-copy">
  <p>We’ve got all the compost, topsoil and garden supplies you’ll need to get your garden in shape this year! Whether you just need some compost to top up your flower beds or want to start growing your own fruit and veg, we have everything you’ll need and much more!</p>
  <p>As the UK’s leading supplier, we have an extensive range of growing media as well as many other garden products such as organic compost, vegetable growing kits and baby vegetable seedlings!</p>
</div>
<div class="abs welcome-photo" role="img" aria-label="Large heap of compost in a yard beside a screening machine and lorry"></div>
<div class="abs readmore">READMORE</div>

<div class="abs footer-rule" style="top:1068px"></div>
<div class="abs brand footer-brand"><span class="brand-mark"></span><span class="brand-name">The Loamfield Store</span></div>
<div class="abs newsletter">SIGN UP FOR NEWSLETTER
  <svg width="17" height="13" viewBox="0 0 17 13"><rect x="1" y="2" width="14" height="10" fill="none" stroke="#7a5a9a" stroke-width="1.2" transform="rotate(-12 8 7)"/><path d="M2 4l7 4 6-6" fill="none" stroke="#7a5a9a" stroke-width="1.1"/></svg>
</div>
<div class="abs send-btn">SEND</div>
<div class="abs social" aria-label="Social links"><span></span><span></span><span></span><span></span></div>
<div class="abs footer-rule" style="top:1140px"></div>
<div class="abs copyright">Copyright © 2014 - All rights reserved.</div>

</body>
</html>
```